Wedding Program

Miriam and Owen are getting married. They are looking for a simple 4-page program that conveys the special day. Venue is a museum in a large East-Coast city: classic 18th century, formal. Ceremony is non-religious. Party includes a photo booth and DJ.

He's a math geek - she's an activist/educator.

Please incorporate unique design sensibility - be creative! Colors of purple, eggplant, ivory, and gray are the couple's choice. Fall motif OK.

Target Market(s)

ages 25 - 85, members of a family

Industry/Entity Type

Graphic Design

Font styles to use
Serif
Decorative

Colors
8769ae
b7a5cd
fece3e
f78f20
757575
cfcfcf
6b449b
a64599
fffaee

Requirements
Must have
• Readable, attractive 4-color design using the copy and image provided in the attachment.
Nice to have
• It's a LOVE-ly day for a wedding - be creative!
Should not have
• Avoid flowery girly-girl fonts or obvious hearts and flowers stuff.

```html
<!DOCTYPE html>
<html lang="en">
<head>
<meta charset="utf-8">
<title>Wedding Program – Miriam &amp; Owen</title>
<link rel="stylesheet" href="https://fonts.googleapis.com/css2?family=EB+Garamond:wght@400;500&family=Petit+Formal+Script&display=swap">
<style>
  :root {
    --ivory: #fff7ec;
    --lace-edge: #fadfbf;
    --lace-mid: rgba(250, 223, 191, 0.6);
    --lace-fade: rgba(250, 223, 191, 0);
    --ink: #35302c;
    --accent: #f28a1f;
  }
  * { box-sizing: border-box; margin: 0; padding: 0; }
  html, body { width: 857px; height: 1200px; overflow: hidden; background: var(--ivory); }
  .program-cover {
    position: relative;
    width: 857px;
    height: 1200px;
    background: var(--ivory);
    overflow: hidden;
  }
  .lace-border {
    position: absolute;
    top: 0;
    width: 320px;
    height: 1200px;
  }
  .lace-border--left {
    left: 0;
    background: linear-gradient(to right, var(--lace-edge) 0%, var(--lace-mid) 60%, var(--lace-fade) 100%);
  }
  .lace-border--right {
    right: 0;
    background: linear-gradient(to left, var(--lace-edge) 0%, var(--lace-mid) 60%, var(--lace-fade) 100%);
  }
  .cover-text {
    position: absolute;
    inset: 0;
    text-align: center;
    color: var(--ink);
    font-family: "EB Garamond", "Times New Roman", serif;
    line-height: 1;
  }
  .cover-text > * { position: absolute; left: 0; right: 0; font-weight: 400; }
  .kicker {
    top: 522px;
    font-size: 34px;
    font-variant: small-caps;
  }
  .couple-name, .couple-and {
    font-family: "Petit Formal Script", cursive;
    color: var(--accent);
  }
  .couple-name { font-size: 58px; }
  .couple-name--first { top: 614px; }
  .couple-and { top: 686px; font-size: 36px; }
  .couple-name--second { top: 730px; }
  .event-date {
    top: 838px;
    font-size: 35px;
    font-variant: small-caps;
  }
  .event-time {
    top: 880px;
    font-size: 33px;
    font-variant: small-caps;
  }
  .venue {
    font-size: 29px;
    font-variant: small-caps;
  }
  .venue--name { top: 966px; }
  .venue--city { top: 1010px; }
</style>
</head>
<body>
  <main class="program-cover">
    <div class="lace-border lace-border--left" role="img" aria-label="Peach lace ornament of flowers and paisley scrolls running down the left edge"></div>
    <div class="lace-border lace-border--right" role="img" aria-label="Peach lace ornament of flowers and paisley scrolls running down the right edge"></div>

    <section class="cover-text">
      <p class="kicker">The Marriage Celebration of</p>
      <h1 class="couple-name couple-name--first">Miriam Ashford</h1>
      <p class="couple-and">and</p>
      <h1 class="couple-name couple-name--second">Owen Delmont</h1>
      <p class="event-date">Saturday, November 1, 2015</p>
      <p class="event-time">At 6 p.m. in the evening</p>
      <p class="venue venue--name">The Hall of Natural Philosophy</p>
      <p class="venue venue--city">Philadelphia Pennsylvania</p>
    </section>
  </main>
</body>
</html>
```